Law firm needs business card and letter head designed

I need a business card and a letter head for a law firm, well its not really a law firm as it is just me.
The letter head is to have the logo located on the top right hand side, with a footer designed as well. The footer will also be on the second page but the main logo design will not be on the second page.

The business card is to be doubled sided.

The business name is Corvane Legal.

Industry/Entity Type

Legal

Requirements
Must have
• The letterhead is to have the logo top right hand side of the front page with email address tbrook@corvanelegal.com.au and phone number 0417 362 851, with a footer designed that incorporates the logo, the footer is also to include the following wording Liability Limited by a scheme approved under Professional Standards Legislation.
• I would like the letterhead design to have a second page, with this page just having the footer design, the second page does not need to have the wording above.
• The business card is to be double sides, with one side having my name Tobias Brook and title Principal, along with the number 0417 362 851 and the email tbrook@corvanelegal.com.au
• I would like a classy design but with some edge.

```html
<!DOCTYPE html>
<html lang="en">
<head>
<meta charset="utf-8">
<title>Corvane Legal — Business Card</title>
<link href="https://fonts.googleapis.com/css2?family=Source+Sans+3:wght@400;600;700&display=swap" rel="stylesheet">
<style>
  :root {
    --backdrop: #141414;
    --teal: #176f8c;
    --teal-deep: #12607a;
    --paper: #ffffff;
    --ink: #2a2a2a;
  }
  * { margin: 0; padding: 0; box-sizing: border-box; }
  html, body {
    width: 1200px; height: 900px; overflow: hidden;
    background: var(--backdrop);
    font-family: "Source Sans 3", "Myriad Pro", Arial, sans-serif;
  }
  .stage { position: relative; width: 1200px; height: 900px; }
  .card {
    position: absolute; top: 170px; width: 347px; height: 561px;
  }
  .card--front { left: 259px; background: var(--paper); color: var(--ink); }
  .card--back { left: 631px; background: var(--teal); }

  .tab {
    position: absolute; left: 102px; width: 143px; background: var(--teal);
  }
  .tab--top { top: 0; height: 30px; }
  .tab--bottom { bottom: 0; height: 28px; }

  .wordmark {
    position: absolute; left: 0; right: 0; text-align: center;
    font-weight: 600; color: var(--teal); letter-spacing: 0.02em;
    text-transform: uppercase; white-space: nowrap;
  }
  .card--front .wordmark { top: 232px; font-size: 33px; }
  .card--back .wordmark { top: 262px; font-size: 33px; color: var(--teal-deep); }

  .holder { position: absolute; top: 336px; left: 0; right: 0; text-align: center; }
  .holder__name { font-size: 20px; font-weight: 700; color: var(--teal); line-height: 1; }
  .holder__title { font-size: 15.5px; font-weight: 400; margin-top: 4px; line-height: 1; }

  .contact { position: absolute; top: 409px; left: 0; right: 0; }
  .contact__row {
    display: flex; align-items: center; justify-content: center;
    gap: 9px; font-size: 16px; line-height: 20px; white-space: nowrap;
  }
  .contact__icon { width: 11px; height: 11px; fill: var(--teal); flex: none; }
</style>
</head>
<body>
<main class="stage">
  <section class="card card--front" aria-label="Business card front">
    <div class="tab tab--top"></div>
    <p class="wordmark">Corvane Legal</p>
    <div class="holder">
      <p class="holder__name">Tobias Brook</p>
      <p class="holder__title">Principal</p>
    </div>
    <div class="contact">
      <p class="contact__row">
        <svg class="contact__icon" viewBox="0 0 24 24" aria-hidden="true"><path d="M6.6 10.8a15.2 15.2 0 0 0 6.6 6.6l2.2-2.2c.3-.3.7-.4 1-.2 1.1.4 2.3.6 3.6.6.6 0 1 .4 1 1V20c0 .6-.4 1-1 1A17 17 0 0 1 3 4c0-.6.4-1 1-1h3.5c.6 0 1 .4 1 1 0 1.3.2 2.5.6 3.6.1.3 0 .7-.2 1z"/></svg>
        <span>0417 362 851</span>
      </p>
      <p class="contact__row">
        <svg class="contact__icon" viewBox="0 0 24 24" aria-hidden="true"><path d="M2 5h20v14H2z M3 6l9 7 9-7" fill="none" stroke="#176f8c" stroke-width="0"/><path d="M2 5h20v2l-10 6L2 7zM2 9l10 6 10-6v10H2z"/></svg>
        <span>tbrook@corvanelegal.com.au</span>
      </p>
    </div>
    <div class="tab tab--bottom"></div>
  </section>

  <section class="card card--back" aria-label="Business card back">
    <p class="wordmark">Corvane Legal</p>
  </section>
</main>
</body>
</html>
```